Velvet corsaro

I want a business card design. the company is an infrastructure development company.

Target Market(s)

Government
real estate investors
real estate clients

Industry/Entity Type

Business

```html
<!DOCTYPE html>
<html lang="en">
<head>
<meta charset="utf-8">
<title>Velvet Corsaro — Business Card</title>
<link rel="stylesheet" href="https://fonts.googleapis.com/css2?family=Gelasio:wght@400;700&display=swap">
<style>
  :root {
    --page: #ffffff;
    --card-edge: #222222;
    --ink: #111111;
    --brand-red: #e8222b;
    --sky-1: #5cc8ea;
    --sky-2: #3b8fe2;
    --sky-3: #2f80e0;
    --sky-4: #1a55d6;
    --red-1: #f2202b;
    --red-2: #e40a0a;
    --red-3: #be0808;
    --red-4: #9c0707;
    --photo-top: #7fb0d6;
    --photo-mid: #b7c2bf;
    --photo-low: #6f8a5e;
  }
  * { margin: 0; padding: 0; box-sizing: border-box; }
  html, body {
    width: 1200px;
    height: 900px;
    overflow: hidden;
    background: var(--page);
  }
  body {
    position: relative;
    font-family: "Gelasio", Georgia, serif;
    color: var(--ink);
  }
  .card {
    position: absolute;
    left: 212px;
    top: 214px;
    width: 776px;
    height: 475px;
    border: 1px solid var(--card-edge);
    background: var(--page);
    overflow: hidden;
  }
  .brand {
    position: absolute;
    left: 56px;
    top: 68px;
    display: flex;
    align-items: center;
    gap: 12px;
  }
  .brand-square {
    width: 22px;
    height: 22px;
    background: var(--brand-red);
  }
  .brand-name {
    font-size: 27px;
    line-height: 30px;
    font-weight: 400;
    color: var(--brand-red);
    letter-spacing: 0.5px;
  }
  .project-strip {
    position: absolute;
    left: 332px;
    top: 51px;
    width: 443px;
    height: 75px;
    background: linear-gradient(180deg, var(--photo-top) 0%, var(--photo-mid) 55%, var(--photo-low) 100%);
  }
  .contact {
    position: absolute;
    font-size: 21px;
    line-height: 29px;
  }
  .contact-person { left: 74px; top: 246px; }
  .contact-office { left: 440px; top: 156px; }
  .person-name { font-weight: 700; font-size: 24px; line-height: 32px; }
  .office-name { font-weight: 700; font-size: 20px; letter-spacing: 0.5px; }
  .office-address { margin-bottom: 7px; }
  .stripe {
    position: absolute;
    left: 0;
    width: 100%;
    display: flex;
  }
  .stripe span { display: block; height: 100%; }
  .stripe-blue { top: 414px; height: 9px; }
  .stripe-red { top: 427px; height: 48px; }
  .seg-a { width: 52px; }
  .seg-b { width: 317px; }
  .seg-c { width: 56px; }
  .seg-d { flex: 1; }
  .stripe-blue .seg-a { background: var(--sky-1); }
  .stripe-blue .seg-b { background: var(--sky-2); }
  .stripe-blue .seg-c { background: var(--sky-3); }
  .stripe-blue .seg-d { background: var(--sky-4); }
  .stripe-red .seg-a { background: var(--red-1); }
  .stripe-red .seg-b { background: var(--red-2); }
  .stripe-red .seg-c { background: var(--red-3); }
  .stripe-red .seg-d { background: var(--red-4); }
</style>
</head>
<body>
  <section class="card">
    <div class="brand">
      <span class="brand-square"></span>
      <div class="brand-name">VELVET<br>CORSARO</div>
    </div>

    <div class="project-strip" role="img" aria-label="Row of four project photographs: office buildings, an apartment block, a riverside landscape and a commercial terrace"></div>

    <div class="contact contact-office">
      <div class="office-name">VELVET CORSARO</div>
      <div class="office-address">
        12 Kolawole street<br>
        Off Adeniyi Link Road<br>
        Ikeja Lagos, Nigeria
      </div>
      <div>+234 13956270</div>
      <div>+234 7081459362</div>
      <div>info@velvetcorsaro.com</div>
      <div>www.velvetcorsaro.com</div>
    </div>

    <div class="contact contact-person">
      <div class="person-name">Tunde Aremu</div>
      <div>MD.</div>
      <div>+234 8051427390</div>
      <div>+234 7038264159</div>
      <div>tunde@velvetcorsaro.com</div>
    </div>

    <div class="stripe stripe-blue">
      <span class="seg-a"></span><span class="seg-b"></span><span class="seg-c"></span><span class="seg-d"></span>
    </div>
    <div class="stripe stripe-red">
      <span class="seg-a"></span><span class="seg-b"></span><span class="seg-c"></span><span class="seg-d"></span>
    </div>
  </section>
</body>
</html>
```